Mobile Recording Studio needs business cards

Open to seeing a creative design, but I want to emphasis my logo and minimize the name/title and company information. Possible a fully black background on card.

My company is a mobile sound recording studio. ok to include a my trailer (actual or cartoon) on the card. My initial thought is more straight forward, but a good design will win me over.

SPECS:
CMYK color mode
High (300ppi) raster effect.
cover bleed area
please deliver: Illustrator file with layers and a pdf at completion.

Name and info for the business card:

Dallin Perry
ADR Mixer

email: Dallin@MixVault.com

address:
248 - 5170 East Hollister
Vancouver, BC V5R 2J4

phone:
604.518.2093 office

website:
www.MixVault.com

FB: @MixVault

Instagram: @TheMixVault

Industry/Entity Type

Television Production

Contact Information for Business Card

Dallin Perry
ADR Mixer

email: Dallin@MixVault.com

address:
248 - 5170 East Hollister
Vancouver, BC V5R 2J4

phone:
604.518.2093 office

website:
www.MixVault.com

FB: @MixVault

Instagram: @TheMixVault

Colors

Designer to choose colors to be used in the design.

Requirements
Must have
• emphasis my logo and minimize the name/title and company information.
• SPECS:
• CMYK color mode
• High (300ppi) raster effect.
• cover bleed area
• please deliver: Illustrator file with layers and a pdf at completion.
Nice to have
• maybe include the following:
• all black background or black theme
• my work trailer (actual or cartoon) refer to Instagram: @TheMixVault

```html
<!DOCTYPE html>
<html lang="en">
<head>
<meta charset="utf-8">
<title>MixVault Business Card</title>
<link href="https://fonts.googleapis.com/css2?family=Roboto:wght@400;500;700&display=swap" rel="stylesheet">
<style>
  :root {
    --backdrop: #c9ccd0;
    --card: #000000;
    --ink: #ffffff;
    --mark: #d6d6d6;
  }
  * { margin: 0; padding: 0; box-sizing: border-box; }
  html, body { width: 1200px; height: 1200px; overflow: hidden; }
  body {
    background: var(--backdrop);
    font-family: "Roboto", Arial, sans-serif;
    color: var(--ink);
    position: relative;
  }
  .card {
    position: absolute;
    left: 250px;
    width: 699px;
    height: 400px;
    background: var(--card);
  }
  .card-front { top: 147px; }
  .card-back { top: 652px; }

  .front-brand {
    position: absolute;
    left: 38px;
    bottom: 52px;
    font-size: 96px;
    font-weight: 700;
    line-height: 1;
    letter-spacing: -2px;
    color: var(--mark);
  }

  .back-brand {
    position: absolute;
    left: 39px;
    top: 52px;
    font-size: 36px;
    font-weight: 700;
    line-height: 1;
    letter-spacing: -0.5px;
    color: var(--ink);
  }

  .person {
    position: absolute;
    left: 459px;
    top: 52px;
    width: 200px;
    text-align: center;
    line-height: 1.15;
  }
  .person-name { font-size: 25px; font-weight: 700; letter-spacing: 0.5px; }
  .person-title { font-size: 21px; font-weight: 500; letter-spacing: 0.3px; }

  .contact-heading {
    position: absolute;
    left: 39px;
    top: 168px;
    width: 619px;
    display: flex;
    align-items: center;
    gap: 14px;
    font-size: 24px;
    font-weight: 400;
  }
  .contact-heading .rule { flex: 1; height: 2px; background: var(--ink); }

  .contact-list {
    position: absolute;
    left: 0;
    top: 203px;
    width: 100%;
    list-style: none;
    text-align: center;
    font-size: 15px;
    letter-spacing: 0.6px;
    line-height: 26.3px;
  }
  .contact-list li { padding-left: 0; }
  .contact-list .contact-email { padding-left: 18px; }

  .footer-rule {
    position: absolute;
    left: 38px;
    top: 319px;
    width: 620px;
    height: 2px;
    background: var(--ink);
  }
  .tagline {
    position: absolute;
    left: 0;
    top: 332px;
    width: 100%;
    text-align: center;
    font-size: 15.5px;
    font-weight: 500;
    letter-spacing: 0.4px;
  }
</style>
</head>
<body>
  <section class="card card-front" aria-label="Card front">
    <div class="front-brand">MixVault</div>
  </section>

  <section class="card card-back" aria-label="Card back">
    <div class="back-brand">MixVault</div>

    <div class="person">
      <div class="person-name">DALLIN PERRY</div>
      <div class="person-title">ADR Mixer</div>
    </div>

    <div class="contact-heading">
      <span class="rule"></span>
      <span class="label">Contact</span>
      <span class="rule"></span>
    </div>

    <ul class="contact-list">
      <li class="contact-email">E:&nbsp; Dallin@MixVault.com</li>
      <li>A: 248 - 5170 East Hollister Vancouver, BC V5R 2J4</li>
      <li>P: 604.518.2093</li>
      <li>W: www.MixVault.com</li>
    </ul>

    <div class="footer-rule"></div>
    <p class="tagline">A mobile ADR studio for Vancouver's Film and Television industry.</p>
  </section>
</body>
</html>
```